Corvane Lift Inc Website Deisgn

We are a new small elevator contracting company.
We would like a full website designed similar to
http://pellusk-lifts.example or https://www.marbolt-hoistworks.example/
In addition to contents found on the above webpages.. we would like a section for project gallery etc.... have fun with it ... make it professional

Target Market(s)

Elevator Consultants - Property managers - Condo Boards - Commercial office buildings

Coding

Coded - Design and coding required

Number of Pages Required

5+ page

Requirements
Must have
• Navigation Bar.. Be view able via mobile ..Should be pictures of Tall Office buildings in background.. Toronto city skyline etc....

Have Fun!

```html
<!DOCTYPE html>
<html lang="en">
<head>
<meta charset="utf-8">
<title>Corvane Lift Inc</title>
<link href="https://fonts.googleapis.com/css2?family=Roboto:wght@400;500;700;900&family=Roboto+Condensed:wght@700&display=swap" rel="stylesheet">
<style>
:root{
  --blue:#0b5fc4;
  --blue-dark:#0a4a9c;
  --navy:#0d1b2e;
  --ink:#1b1b1b;
  --muted:#6b7280;
  --pale:#eaf3fd;
  --line:#cfd8e3;
  --white:#ffffff;
  --dark:#111418;
}
*{box-sizing:border-box;margin:0;padding:0}
html,body{width:1200px;height:4624px;overflow:hidden}
body{font-family:'Roboto',Arial,sans-serif;color:var(--ink);background:var(--white);position:relative}
.abs{position:absolute}
.btn{display:inline-block;background:var(--blue);color:var(--white);font-weight:700;font-size:15px;letter-spacing:.5px;text-transform:uppercase;padding:12px 26px;border-radius:3px}
.eyebrow{color:var(--blue);font-size:15px;letter-spacing:1px;text-transform:uppercase;text-align:center}
.section-title{font-family:'Roboto Condensed','Roboto',sans-serif;font-size:44px;font-weight:700;text-transform:uppercase;text-align:center;color:var(--ink)}
.brand-name{font-family:'Roboto',sans-serif;font-weight:900;font-size:26px;letter-spacing:1px;color:var(--ink);display:flex;align-items:center;gap:10px}
.brand-name .dot{width:30px;height:30px;border-radius:50%;background:var(--blue);display:inline-block}

/* header */
.site-header{top:0;left:0;width:1200px;height:68px;background:var(--white);display:flex;align-items:center;justify-content:space-between;padding:0 72px}
.main-nav{display:flex;align-items:center;gap:26px;font-size:15px;font-weight:500;text-transform:uppercase}
.main-nav .active{color:var(--blue)}
.main-nav .btn{padding:9px 18px;font-size:14px}

/* hero */
.hero{top:68px;left:0;width:1200px;height:604px;background:linear-gradient(180deg,#2a3a4f 0%,#1c2635 55%,#0f141c 100%);overflow:hidden}
.hero-copy{left:72px;top:190px;color:var(--white)}
.hero-copy h1{font-size:44px;line-height:1.22;font-weight:900;text-transform:uppercase}
.hero-copy h1 .hl{color:#3f8df0}
.hero-copy .loc{font-size:15px;margin-top:10px;letter-spacing:.5px}
.hero-copy .btn{margin-top:40px}
.hero-arrow{top:290px;width:40px;height:40px;border-radius:50%;background:rgba(255,255,255,.25)}
.badge{width:84px;height:84px;border-radius:50%;background:var(--white);display:flex;align-items:center;justify-content:center}
.badge span{width:60px;height:60px;border-radius:50%;background:var(--blue);display:block}

/* about */
.about-head{top:768px;left:0;width:1200px;text-align:center}
.about-head .section-title{font-size:40px;margin-top:8px}
.about-head .sub{font-size:15px;margin-top:6px;text-transform:uppercase}
.about-photo{left:200px;top:912px;width:320px;height:424px;background:linear-gradient(160deg,#7aa6d6,#2e5a8e 60%,#1d3a5f)}
.about-inset{width:112px;height:112px;border-radius:50%;border:5px solid var(--white)}
.about-copy{left:664px;top:944px;width:500px;font-size:15px;line-height:1.75;color:var(--muted)}
.about-copy p{margin-bottom:20px}
.about-copy .strong{color:var(--ink);font-weight:500}

/* services */
.services-head{top:1412px;left:0;width:1200px}
.services-head .section-title{margin-top:8px}
.service-grid{top:1532px;left:110px;width:980px;display:flex;gap:12px}
.service{width:236px;height:334px;padding:34px 24px;text-align:center;background:var(--white)}
.service.featured{background:var(--blue);color:var(--white);border-radius:4px;box-shadow:0 6px 18px rgba(11,95,196,.3)}
.service svg{width:80px;height:80px}
.service h3{font-size:16px;font-weight:700;text-transform:uppercase;margin:24px 0 26px;line-height:1.3}
.service p{font-size:14px;line-height:1.6;color:var(--muted)}
.service.featured p{color:#dbe8fa}
.service .arrow{margin-top:20px;font-size:22px;color:var(--blue)}
.service.featured .arrow{color:var(--white)}

/* cta */
.cta{top:1968px;left:0;width:1200px;height:340px;background:linear-gradient(180deg,#0d1117,#1a2230 50%,#0d1117);color:var(--white);text-align:center}
.cta h2{padding-top:100px;font-size:40px;font-weight:700}
.cta p{width:640px;margin:20px auto 0;font-size:15px;line-height:1.6;color:#c8d0dc}
.cta .btn{margin-top:30px}

/* gallery */
.gallery{top:2308px;left:0;width:1200px;height:600px;background:var(--pale)}
.gallery .eyebrow{margin-top:76px}
.gallery .section-title{margin-top:6px}
.gallery-row{top:172px;left:140px;display:flex;gap:20px}
.gallery-item{width:292px;height:288px}
.dots{top:488px;left:0;width:1200px;display:flex;justify-content:center;gap:10px}
.dots span{width:24px;height:4px;background:#9cb9de}
.dots span.on{background:var(--blue);width:32px}

/* testimonial */
.testimonial{top:2908px;left:0;width:1200px;height:404px;text-align:center}
.avatars{top:46px;left:0;width:1200px;display:flex;justify-content:center;gap:22px;align-items:center}
.avatars span{border-radius:50%;background:linear-gradient(180deg,#d9c4b0,#8a7260)}
.quote{top:158px;left:270px;width:660px;font-style:italic;font-size:17px;line-height:1.7;color:#333}
.stars{top:286px;left:0;width:1200px;color:var(--blue);font-size:18px;letter-spacing:4px}
.client{top:318px;left:0;width:1200px;color:var(--blue);font-weight:700;font-size:14px;text-transform:uppercase}
.t-arrow{top:180px;color:#9aa3ad;font-size:34px}

/* faq */
.faq{top:3312px;left:0;width:1200px;height:548px;background:var(--pale)}
.faq-panel{left:0;top:0;width:420px;height:548px;background:var(--blue)}
.faq-photo{left:240px;top:88px;width:360px;height:360px;border-radius:50%;background:linear-gradient(170deg,#c9d9ea,#6d8fb3 55%,#2b3d55);border:8px solid var(--white)}
.faq-title{left:668px;top:56px;font-family:'Roboto Condensed','Roboto',sans-serif;font-size:40px;line-height:1.15;font-weight:700;text-transform:uppercase}
.faq-list{left:668px;top:196px;width:420px}
.faq-item{background:var(--white);border:1px solid var(--line);margin-bottom:14px;padding:16px 18px;font-size:14px;display:flex;justify-content:space-between;align-items:flex-start;border-radius:3px}
.faq-item.open{border-color:var(--blue);flex-wrap:wrap}
.faq-item .q{color:var(--ink)}
.faq-item.open .q{color:var(--blue)}
.faq-item .sign{color:var(--blue);font-size:20px;line-height:14px}
.faq-item .a{width:100%;margin-top:12px;padding-top:12px;border-top:1px solid var(--line);color:var(--muted);line-height:1.6}

/* quote form */
.quote-form{top:3860px;left:0;width:1200px;height:460px}
.quote-form .eyebrow{margin-top:62px}
.quote-form .section-title{margin-top:6px}
.field{border:1px solid var(--line);border-radius:3px;height:48px;padding:14px 16px;font-size:13px;color:var(--muted)}
.field.focus{border-color:var(--blue)}
.send{top:372px;left:0;width:1200px;text-align:center}

/* contact */
.contact-band{top:4320px;left:0;width:1200px;height:180px;background:var(--pale)}
.contact-col{width:240px;text-align:center;top:30px}
.contact-col .ic{width:60px;height:60px;border-radius:50%;background:var(--blue);margin:0 auto;display:flex;align-items:center;justify-content:center}
.contact-col h4{margin-top:14px;font-size:16px;font-weight:700}
.contact-col p{margin-top:6px;font-size:13px;color:var(--muted)}

/* footer */
.site-footer{top:4500px;left:0;width:1200px;height:124px;background:var(--dark);color:var(--white)}
.site-footer .brand-name{color:var(--white);position:absolute;left:20px;top:22px}
.footer-links{position:absolute;left:366px;top:34px;font-size:14px;color:#d5d9df}
.copyright{position:absolute;left:366px;top:68px;font-size:13px;color:#9aa2ad}
.socials{position:absolute;right:30px;top:30px;display:flex;gap:12px}
.socials span{width:36px;height:36px;border-radius:50%;border:2px solid var(--blue)}
</style>
</head>
<body>

<header class="site-header abs">
  <div class="brand-name"><span class="dot"></span>CORVANE LIFT INC</div>
  <nav class="main-nav">
    <span class="active">• Home</span><span>About</span><span>Services</span><span>Gallery</span><span>FAQ</span><span>Contact</span>
    <span class="btn">Free Quote</span>
  </nav>
</header>

<section class="hero abs" role="img" aria-label="Toronto city skyline at dusk with tall office towers">
  <div class="hero-copy abs">
    <h1>Next level services<br><span class="hl">maintanence</span> for the<br>elevator industry</h1>
    <p class="loc">TORONTO ONTARIO CANADA</p>
    <span class="btn">Contact Us</span>
  </div>
  <span class="hero-arrow abs" style="left:-20px"></span>
  <span class="hero-arrow abs" style="right:-20px"></span>
  <svg class="abs" style="left:0;top:520px" width="1200" height="84" viewBox="0 0 1200 84">
    <polygon points="0,84 1200,84 1200,40 0,84" fill="#ffffff"/>
    <polygon points="760,84 1200,10 1200,84" fill="#0b5fc4"/>
  </svg>
</section>
<div class="badge abs" style="left:558px;top:630px"><span></span></div>

<section class="about-head abs">
  <p class="eyebrow">About Us</p>
  <h2 class="section-title">Corvane Lift</h2>
  <p class="sub">Toronto Ontario Canada</p>
</section>
<div class="about-photo abs" role="img" aria-label="Glass office towers viewed from below"></div>
<div class="about-inset abs" role="img" aria-label="Technician in hard hat" style="left:130px;top:990px;background:linear-gradient(180deg,#e4c87a,#6f8fb0)"></div>
<div class="about-inset abs" role="img" aria-label="Engineer at work" style="left:470px;top:1250px;background:linear-gradient(180deg,#8aa0bd,#33475f)"></div>
<div class="about-copy abs">
  <p>Lorem Ipsum is simply dummy text of the printing and typesetting industry. Lorem Ipsum has been the industry's standard dummy text ever since.</p>
  <p>Lorem Ipsum is simply dummy text of the printing and typesetting industry. Lorem Ipsum has been the industry's standard dummy text ever since. Lorem Ipsum is simply dummy text of the printing and.</p>
  <p class="strong">Lorem Ipsum is simply dummy text of the printing and typesetting industry Lorem Ipsum.</p>
  <span class="btn">Learn More</span>
</div>

<section class="services-head abs">
  <p class="eyebrow">What We Do</p>
  <h2 class="section-title">Services We Provided</h2>
</section>
<div class="service-grid abs">
  <article class="service">
    <svg viewBox="0 0 80 80" fill="none" stroke="#1b2a44" stroke-width="3"><circle cx="40" cy="40" r="14"/><circle cx="40" cy="40" r="26" stroke-dasharray="8 6"/><circle cx="40" cy="40" r="5" fill="#1b2a44"/></svg>
    <h3>Modernization</h3>
    <p>Lorem Ipsum is simply the dummy text of the printing setting industry.</p>
    <div class="arrow">⟶</div>
  </article>
  <article class="service featured">
    <svg viewBox="0 0 80 80" fill="none" stroke="#ffffff" stroke-width="3"><rect x="14" y="8" width="52" height="64" rx="3"/><line x1="40" y1="8" x2="40" y2="72"/><path d="M24 30l5-6 5 6M46 44l5 6 5-6"/></svg>
    <h3>Maintenance</h3>
    <p>Lorem Ipsum is simply the dummy text of the printing setting industry.</p>
    <div class="arrow">⟶</div>
  </article>
  <article class="service">
    <svg viewBox="0 0 80 80" fill="none" stroke="#1b2a44" stroke-width="4" stroke-linecap="round"><line x1="18" y1="62" x2="58" y2="22"/><circle cx="62" cy="18" r="8"/><line x1="20" y1="20" x2="60" y2="60"/><rect x="12" y="12" width="12" height="12" transform="rotate(45 18 18)"/></svg>
    <h3>Service &amp; Repair</h3>
    <p>Lorem Ipsum is simply the dummy text of the printing setting industry.</p>
    <div class="arrow">⟶</div>
  </article>
  <article class="service">
    <svg viewBox="0 0 80 80" fill="none" stroke="#1b2a44" stroke-width="3"><line x1="8" y1="30" x2="72" y2="30"/><line x1="8" y1="50" x2="72" y2="50"/><line x1="16" y1="18" x2="16" y2="66"/><line x1="32" y1="18" x2="32" y2="66"/><line x1="48" y1="18" x2="48" y2="66"/><line x1="64" y1="18" x2="64" y2="66"/></svg>
    <h3>Top of Car Guard<br>Rail Installation</h3>
    <p>Lorem Ipsum is simply the dummy text of the printing setting industry.</p>
    <div class="arrow">⟶</div>
  </article>
</div>

<section class="cta abs" role="img" aria-label="Dark elevator shaft perspective">
  <h2>Are you Ready for Corvane Lift ?</h2>
  <p>Lorem Ipsum is simply dummy text of the printing and typesetting industry. Lorem Ipsum has been the industry's standard dummy...</p>
  <span class="btn">Contact Us</span>
</section>
<div class="badge abs" style="left:558px;top:1926px"><span></span></div>

<section class="gallery abs">
  <p class="eyebrow">Work</p>
  <h2 class="section-title">Our Gallery</h2>
  <div class="gallery-row abs">
    <div class="gallery-item" role="img" aria-label="Wood-panelled elevator lobby" style="background:linear-gradient(90deg,#c49a6c,#8a6440 50%,#d8c2a4)"></div>
    <div class="gallery-item" role="img" aria-label="Row of steel elevator doors in a lobby" style="background:linear-gradient(180deg,#5d6e82,#2f3d4f 60%,#8c8f92)"></div>
    <div class="gallery-item" role="img" aria-label="Stainless elevator doors in a bright hall" style="background:linear-gradient(180deg,#dfe3e8,#9aa3ae 60%,#6a5a50)"></div>
  </div>
  <div class="dots abs"><span class="on"></span><span></span><span></span><span></span></div>
</section>

<section class="testimonial abs">
  <div class="avatars abs">
    <span role="img" aria-label="Client portrait" style="width:60px;height:60px"></span>
    <span role="img" aria-label="Client portrait" style="width:76px;height:76px"></span>
    <span role="img" aria-label="Client portrait" style="width:60px;height:60px"></span>
  </div>
  <p class="quote abs">" Lorem Ipsum is simply dummy text of the printing and typesetting industry. Lorem Ipsum has been the industry's standard dummy text ever since the 1500s, when an unknown printer took a galley scrambled. "</p>
  <div class="stars abs">★★★★★</div>
  <div class="client abs">Client Name</div>
  <span class="t-arrow abs" style="left:160px">‹</span>
  <span class="t-arrow abs" style="right:160px">›</span>
</section>

<section class="faq abs">
  <div class="faq-panel abs"></div>
  <div class="faq-photo abs" role="img" aria-label="Two businessmen in suits talking outside an office building"></div>
  <h2 class="faq-title abs">Frequently Asked<br>Questions</h2>
  <div class="faq-list abs">
    <div class="faq-item open"><span class="q">Lorem Ipsum is simply dummy text ?</span><span class="sign">−</span><p class="a">Lorem Ipsum is simply dummy text of the printing and typesetting industry.</p></div>
    <div class="faq-item"><span class="q">Lorem Ipsum is simply dummy text ?</span><span class="sign">+</span></div>
    <div class="faq-item"><span class="q">Lorem Ipsum is simply dummy text ?</span><span class="sign">+</span></div>
  </div>
</section>

<section class="quote-form abs">
  <p class="eyebrow">Get In Touch</p>
  <h2 class="section-title">Get a Free Quote</h2>
  <div class="field focus abs" style="left:180px;top:168px;width:272px">Name *</div>
  <div class="field abs" style="left:468px;top:168px;width:272px">Email *</div>
  <div class="field abs" style="left:756px;top:168px;width:264px">Phone *</div>
  <div class="field abs" style="left:180px;top:232px;width:840px;height:100px">Message *</div>
  <div class="send abs"><span class="btn">Send a Message</span></div>
</section>

<section class="contact-band abs">
  <div class="contact-col abs" style="left:188px">
    <div class="ic"><svg width="26" height="26" viewBox="0 0 24 24" fill="#fff"><path d="M6.6 10.8a15 15 0 0 0 6.6 6.6l2.2-2.2c.3-.3.7-.4 1-.2 1.1.4 2.3.6 3.6.6.6 0 1 .4 1 1V20c0 .6-.4 1-1 1A17 17 0 0 1 3 4c0-.6.4-1 1-1h3.5c.6 0 1 .4 1 1 0 1.3.2 2.5.6 3.6.1.3 0 .7-.2 1z"/></svg></div>
    <h4>Main</h4><p>(555) 014-2270</p>
  </div>
  <div class="contact-col abs" style="left:480px">
    <div class="ic"><svg width="26" height="26" viewBox="0 0 24 24" fill="#fff"><path d="M6.6 10.8a15 15 0 0 0 6.6 6.6l2.2-2.2c.3-.3.7-.4 1-.2 1.1.4 2.3.6 3.6.6.6 0 1 .4 1 1V20c0 .6-.4 1-1 1A17 17 0 0 1 3 4c0-.6.4-1 1-1h3.5c.6 0 1 .4 1 1 0 1.3.2 2.5.6 3.6.1.3 0 .7-.2 1z"/></svg></div>
    <h4>Cell</h4><p>(555) 019-4481</p>
  </div>
  <div class="contact-col abs" style="left:768px">
    <div class="ic"><svg width="26" height="26" viewBox="0 0 24 24" fill="#fff"><path d="M3 5h18v14H3z" fill="none" stroke="#fff" stroke-width="2"/><path d="M3 6l9 7 9-7" fill="none" stroke="#fff" stroke-width="2"/></svg></div>
    <h4>Email</h4><p>hello@corvanelift.example</p>
  </div>
</section>

<footer class="site-footer abs">
  <div class="brand-name"><span class="dot"></span>CORVANE LIFT INC</div>
  <p class="footer-links">Home &nbsp;|&nbsp; About &nbsp;|&nbsp; Services &nbsp;|&nbsp; Gallery &nbsp;|&nbsp; Faq &nbsp;|&nbsp; Free Quote &nbsp;|&nbsp; Contact</p>
  <p class="copyright">©Corvane Lift · 2020 All rights reserved</p>
  <div class="socials"><span></span><span></span><span></span></div>
</footer>

</body>
</html>
```